Brightwell Bonds and Households Initiative

We need a flyer that invites low-income Spanish speaking individuals to our program. The program is 12 weeks. We offer healthy relationship education, and financial stability. We also touch on workforce development. These workshops are for couples only.

We are in five locations, so we need a flyer that we can change the text to be able to update the address, dates and any additional information based on our needs.

Attached is the logo we would like to use. I have also attached a previous flyer that we created to give you an idea of the text that is included.

Target Market(s)

We are reaching out to low income adult couples

Font styles to use
Serif

Requirements
Must have
• This flyer must catch the eye of couples wanting to improve their relationship, and finances.
Nice to have
• Some space for us to plug in dates location and times. This flyer also has to have our funding statement at the bottom.

```html
<!DOCTYPE html>
<html lang="es">
<head>
<meta charset="utf-8">
<title>Talleres Para Parejas – Lazos y Hogares Brightwell</title>
<link rel="stylesheet" href="https://fonts.googleapis.com/css2?family=Mulish:wght@700;800&family=Cormorant+Garamond:ital,wght@1,500&family=Source+Sans+3:ital,wght@0,400;0,600;0,700;1,400&display=swap">
<style>
  :root {
    --orange: #f47a20;
    --red-orange: #f04e1e;
    --frame: #ee4a24;
    --teal-band: #93cfcf;
    --mint-script: #b3e0d6;
    --ink: #111111;
    --white: #ffffff;
    --sunset-core: #f3b25c;
    --sunset-mid: #c98a55;
    --sunset-edge: #6f6a48;
  }
  * { box-sizing: border-box; margin: 0; padding: 0; }
  html, body { width: 900px; height: 1200px; overflow: hidden; background: var(--white); }
  .flyer { position: relative; width: 900px; height: 1200px; background: var(--white); font-family: "Source Sans 3", Arial, sans-serif; color: var(--ink); }

  .hero { position: absolute; left: 0; top: 0; width: 900px; height: 450px; overflow: hidden; }
  .hero-photo {
    position: absolute; inset: 0;
    background:
      radial-gradient(ellipse 28% 40% at 50% 45%, #fbd38a 0%, rgba(243,178,92,0.85) 35%, rgba(201,138,85,0) 75%),
      linear-gradient(90deg, #e9e4dc 0%, #d9d2c6 9%, var(--sunset-edge) 16%, var(--sunset-mid) 32%, var(--sunset-core) 50%, var(--sunset-mid) 68%, var(--sunset-edge) 84%, #d9d2c6 91%, #e9e4dc 100%);
  }
  .hero-title {
    position: absolute; left: 0; right: 0; top: 196px; text-align: center;
    font-family: "Mulish", "Century Gothic", sans-serif; font-weight: 800;
    font-size: 68px; letter-spacing: 1px; color: var(--orange);
  }
  .hero-tagline {
    position: absolute; left: 0; right: 0; top: 268px; text-align: center;
    font-family: "Cormorant Garamond", Georgia, serif; font-style: italic; font-weight: 500;
    font-size: 35px; line-height: 44px; color: var(--mint-script);
  }

  .details-frame {
    position: absolute; left: 51px; top: 485px; width: 797px; height: 382px;
    border: 3px solid var(--frame); border-top: none;
  }
  .frame-top { position: absolute; top: 0; height: 3px; background: var(--frame); }
  .frame-top.left { left: 0; width: 253px; }
  .frame-top.right { right: 0; width: 280px; }

  .brand {
    position: absolute; left: 300px; top: 508px; width: 300px; height: 60px;
    display: flex; align-items: center; justify-content: center; gap: 10px;
  }
  .brand-dot { width: 26px; height: 26px; border-radius: 50%; background: var(--orange); flex: none; }
  .brand-name { font-family: "Source Sans 3", Arial, sans-serif; font-weight: 600; font-size: 27px; color: var(--orange); white-space: nowrap; }

  .schedule { position: absolute; left: 51px; width: 797px; top: 596px; text-align: center; }
  .schedule .label { font-weight: 700; font-size: 22px; line-height: 30px; }
  .schedule .value { font-style: italic; font-size: 22px; line-height: 30px; }
  .schedule .note { font-weight: 700; font-size: 21px; line-height: 30px; color: var(--red-orange); }

  .topics { position: absolute; left: 0; top: 889px; width: 900px; height: 311px; background: var(--teal-band); }
  .topics-heading { position: absolute; left: 71px; top: 14px; font-weight: 700; font-size: 22px; color: var(--ink); }
  .topic-list { position: absolute; left: 62px; top: 48px; list-style: none; }
  .topic-list li { display: flex; align-items: center; gap: 9px; height: 31px; font-size: 20px; color: var(--red-orange); }
  .topic-list svg { width: 20px; height: 20px; flex: none; }
  .funding {
    position: absolute; left: 20px; right: 20px; top: 270px; text-align: center;
    font-weight: 700; font-size: 10.5px; line-height: 15px; color: var(--ink);
  }
</style>
</head>
<body>
<div class="flyer">
  <header class="hero">
    <div class="hero-photo" role="img" aria-label="Fotografía de una pareja tomada de la mano frente a un atardecer dorado entre árboles"></div>
    <h1 class="hero-title">Talleres Para Parejas</h1>
    <p class="hero-tagline">Porque una relación sana esta<br>“A Nuestro Alcance”</p>
  </header>

  <div class="details-frame">
    <span class="frame-top left"></span>
    <span class="frame-top right"></span>
  </div>

  <div class="brand">
    <span class="brand-dot"></span>
    <span class="brand-name">Lazos y Hogares Brightwell</span>
  </div>

  <section class="schedule">
    <p class="label">Fecha de talleres:</p>
    <p class="value">jueves octubre 03, 12, 19, 26</p>
    <p class="label">Horario:</p>
    <p class="value">5:30pm –8:00pm</p>
    <p class="label">Ubicación:</p>
    <p class="value">Linden Grove Family Resource Center</p>
    <p class="value">4820 Linden Ave, Fairhaven CA 90000</p>
    <p class="value">(555) 014-2286</p>
    <p class="note">*Cuidado de niños y cena será proporcionado</p>
  </section>

  <section class="topics">
    <h2 class="topics-heading">TEMAS INCLUYEN:</h2>
    <ul class="topic-list">
      <li><svg viewBox="0 0 20 20"><circle cx="10" cy="10" r="8" fill="none" stroke="#111" stroke-width="1.8"/><path d="M6 10.3l2.8 2.7L14.2 7.4" fill="none" stroke="#111" stroke-width="2"/></svg>Llaves para la buena  communicación</li>
      <li><svg viewBox="0 0 20 20"><circle cx="10" cy="10" r="8" fill="none" stroke="#111" stroke-width="1.8"/><path d="M6 10.3l2.8 2.7L14.2 7.4" fill="none" stroke="#111" stroke-width="2"/></svg>Tipos de personalidad y expectativas</li>
      <li><svg viewBox="0 0 20 20"><circle cx="10" cy="10" r="8" fill="none" stroke="#111" stroke-width="1.8"/><path d="M6 10.3l2.8 2.7L14.2 7.4" fill="none" stroke="#111" stroke-width="2"/></svg>Señales de peligro en una relación</li>
      <li><svg viewBox="0 0 20 20"><circle cx="10" cy="10" r="8" fill="none" stroke="#111" stroke-width="1.8"/><path d="M6 10.3l2.8 2.7L14.2 7.4" fill="none" stroke="#111" stroke-width="2"/></svg>Técnicas para formar y  sostener una relación sana</li>
      <li><svg viewBox="0 0 20 20"><circle cx="10" cy="10" r="8" fill="none" stroke="#111" stroke-width="1.8"/><path d="M6 10.3l2.8 2.7L14.2 7.4" fill="none" stroke="#111" stroke-width="2"/></svg>Resolucion de problemas</li>
      <li><svg viewBox="0 0 20 20"><circle cx="10" cy="10" r="8" fill="none" stroke="#111" stroke-width="1.8"/><path d="M6 10.3l2.8 2.7L14.2 7.4" fill="none" stroke="#111" stroke-width="2"/></svg>Como mantener la diversion</li>
      <li><svg viewBox="0 0 20 20"><circle cx="10" cy="10" r="8" fill="none" stroke="#111" stroke-width="1.8"/><path d="M6 10.3l2.8 2.7L14.2 7.4" fill="none" stroke="#111" stroke-width="2"/></svg>Como adminstrar el dinero entre pareja y muchos mas</li>
    </ul>
    <p class="funding">“Funding for this project was provided by the Northfield Community Trust, Office for Families and Households, Grant: #90ZZ0000.<br>These services are available to all eligible persons, regardless of race, gender, age, disability, or religion.”</p>
  </section>
</div>
</body>
</html>
```